Ashby Meadows Thank-You Tag

Looking for a file that incorporates current branding/colors and says:

"Thanks for Swimming with Us!"
Ashby Meadows Otters

Samples of other pieces we've done recently are attached.

Will be printed on cardstock that is
Width: 3.5 inches
Height: 2.5 inches

```html
<!DOCTYPE html>
<html lang="en">
<head>
<meta charset="utf-8">
<title>Ashby Meadows Otters – Thank-You Tag</title>
<link rel="stylesheet" href="https://fonts.googleapis.com/css2?family=Nunito:wght@900&family=Lobster&display=swap">
<style>
  :root {
    --backdrop: #333130;
    --pool-blue: #2b52a3;
    --splash-pink: #ef5b9c;
    --sky-blue: #8bbde6;
    --white: #ffffff;
    --dolphin-grey: #c4c6cc;
  }
  html, body {
    margin: 0;
    width: 1200px;
    height: 901px;
    overflow: hidden;
    background: var(--backdrop);
  }
  .tag {
    position: absolute;
    left: 100px;
    top: 94px;
    width: 999px;
    height: 714px;
    background: var(--pool-blue);
    overflow: hidden;
  }
  .tag-art {
    position: absolute;
    inset: 0;
  }
  .headline {
    position: absolute;
    margin: 0;
    line-height: 1;
    text-align: center;
    white-space: nowrap;
    transform-origin: center center;
  }
  .headline-thanks {
    left: 225px;
    top: 162px;
    width: 600px;
    font-family: "Nunito", sans-serif;
    font-weight: 900;
    font-size: 76px;
    letter-spacing: -1.5px;
    color: var(--white);
    transform: rotate(-2.4deg);
  }
  .headline-swimming {
    left: 74px;
    top: 233px;
    width: 900px;
    font-family: "Nunito", sans-serif;
    font-weight: 900;
    font-size: 130px;
    letter-spacing: -1px;
    color: var(--splash-pink);
    transform: rotate(-2.4deg);
  }
  .headline-with-us {
    left: 222px;
    top: 331px;
    width: 600px;
    font-family: "Lobster", cursive;
    font-size: 115px;
    color: var(--white);
    transform: rotate(-2.4deg);
  }
  .team-name {
    position: absolute;
    left: 227px;
    top: 471px;
    width: 600px;
    margin: 0;
    font-family: "Nunito", sans-serif;
    font-weight: 900;
    font-size: 37px;
    line-height: 1;
    color: var(--white);
    text-align: center;
    letter-spacing: -0.5px;
    white-space: nowrap;
    transform: rotate(-2.3deg);
  }
  .art-dolphin-left,
  .art-dolphin-right,
  .art-splash-top {
    position: absolute;
  }
  .art-dolphin-left {
    left: 76px; top: 398px; width: 157px; height: 213px;
    border-radius: 50% 50% 40% 40%;
    background: linear-gradient(160deg, var(--dolphin-grey), #9aa3bd);
    opacity: 0.9;
  }
  .art-dolphin-right {
    left: 828px; top: 473px; width: 121px; height: 166px;
    border-radius: 50% 50% 40% 40%;
    background: linear-gradient(200deg, var(--dolphin-grey), #9aa3bd);
    opacity: 0.9;
  }
  .art-splash-top {
    left: 420px; top: 92px; width: 196px; height: 62px;
    border-radius: 50% 50% 30% 30%;
    background: radial-gradient(ellipse at 50% 100%, var(--sky-blue), rgba(139,189,230,0.3));
  }
</style>
</head>
<body>
<div class="tag">
  <svg class="tag-art" viewBox="0 0 999 714" width="999" height="714" aria-hidden="true">
    <path class="frame-line" d="M27 602 V129 Q27 29 127 29 H873 Q973 29 973 129 V602" fill="none" stroke="var(--sky-blue)" stroke-width="2.5"/>
    <line class="accent-dash" x1="206" y1="216" x2="265" y2="213" stroke="var(--splash-pink)" stroke-width="3"/>
    <line class="accent-dash" x1="782" y1="187" x2="838" y2="185" stroke="var(--splash-pink)" stroke-width="3"/>
    <path class="ribbon" d="M230 478 L817 456 L800 487 L817 517 L232 538 L252 508 Z" fill="var(--splash-pink)"/>
    <path class="wave-white" d="M0 586 Q37.5 574 75 586 T150 586 T225 586 T300 586 T375 586 T450 586 T525 586 T600 586 T675 586 T750 586 T825 586 T900 586 T975 586 T1050 586 V714 H0 Z" fill="var(--white)"/>
    <path class="wave-sky" d="M0 605 Q37.5 593 75 605 T150 605 T225 605 T300 605 T375 605 T450 605 T525 605 T600 605 T675 605 T750 605 T825 605 T900 605 T975 605 T1050 605 V714 H0 Z" fill="var(--sky-blue)"/>
    <path class="wave-deep" d="M0 617 Q37.5 605 75 617 T150 617 T225 617 T300 617 T375 617 T450 617 T525 617 T600 617 T675 617 T750 617 T825 617 T900 617 T975 617 T1050 617 V714 H0 Z" fill="var(--pool-blue)"/>
    <path class="wave-pink" d="M0 623 Q37.5 611 75 623 T150 623 T225 623 T300 623 T375 623 T450 623 T525 623 T600 623 T675 623 T750 623 T825 623 T900 623 T975 623 T1050 623 V714 H0 Z" fill="var(--splash-pink)"/>
  </svg>

  <div class="art-splash-top" role="img" aria-label="Water splash droplets above the headline"></div>
  <div class="art-dolphin-left" role="img" aria-label="Illustrated dolphin leaping out of the water"></div>
  <div class="art-dolphin-right" role="img" aria-label="Illustrated dolphin diving into the water"></div>

  <p class="headline headline-thanks">THANKS FOR</p>
  <p class="headline headline-swimming">SWIMMING</p>
  <p class="headline headline-with-us">with Us!</p>
  <p class="team-name">ASHBY MEADOWS OTTERS</p>
</div>
</body>
</html>
```